Design New Business Card, Envelope and Letter Head !

We need a stationery design for our newly developed logo! We need professional classic look.

Front of the Card:
Logo on the left hand side

Personal Detail in the right hand side
i.e. Name,
Title
Office:
Cell:
Fax:
email:

www.torvanlending.example

Color Scheme should match our logo.

Back Side of the Card:

Logo again with Green back ground or off gray back ground ( Note: Color has to be from logo)

and below message. Again, font size and color should come from logo.

" Manifest your trust in us through the gift of your referrals. We won't let you down."
Updates

Dear Designers;

We have updates few info which we missed earlier. Please include those words in the logo and resubmit your designs for consideration.  We are looking for very professional and classic look. Thanks for your great creation. I have changed the payment options. Please have a look and best of luck.

Ned

Dear All Designers:

For address; please use following address:

" 4172 Willow Crest Ln, San Ramon, CA 94583 " 
Please do not use the address in the website. We would like to give business card with option of calling us is the top priority then email then qLine. Please make sure Put " qLine" in the business card. 

Reason: Since I have updated some information per requirements, I would like to give enough time for the great design work.

Just a note to all designers:

"Equal Opportunity Lender" Sign has to be in back  of the card  in a small image. I would say it has to be "inconspicuous". Let's put the HRQA # and StaPLO # in front side. Let's organise the information follow very elegant and professional.

Requirements
Must have
• We must need following Words in the business card

StaPLO License #

HRQA #

And the logo of " Equal Housing Lender ". Please see the logo attached.

Please put these words or logo represents above at the right location of the card.

```html
<!DOCTYPE html>
<html lang="en">
<head>
<meta charset="utf-8">
<title>Torvan Lending – Business Card</title>
<link href="https://fonts.googleapis.com/css2?family=Raleway:wght@300;400&family=Tinos:wght@400&display=swap" rel="stylesheet">
<style>
  :root {
    --backdrop: #c3e9e4;
    --card-light: #f7f7f5;
    --card-dark: #3b3b3d;
    --brand-green: #5fae55;
    --ink-gray: #5a5a5c;
    --ink-soft: #7a7a7c;
    --paper-white: #f4f4f2;
    --rule-gray: #9a9a9a;
  }
  html, body {
    margin: 0;
    padding: 0;
    width: 1200px;
    height: 1091px;
    overflow: hidden;
    background: var(--backdrop);
  }
  .stage {
    width: 1200px;
    height: 1091px;
    display: flex;
    align-items: center;
    justify-content: center;
    gap: 50px;
  }
  .card {
    position: relative;
    width: 540px;
    height: 310px;
    box-sizing: border-box;
    box-shadow: 0 18px 40px rgba(40, 90, 85, 0.25);
  }

  /* Front */
  .card-front {
    background: var(--card-light);
    border-bottom: 3px solid var(--brand-green);
  }
  .front-brand {
    position: absolute;
    left: 44px;
    top: 132px;
    display: flex;
    align-items: center;
    gap: 10px;
  }
  .brand-square {
    width: 14px;
    height: 14px;
    background: var(--brand-green);
  }
  .front-brand .brand-name {
    font-family: "Tinos", serif;
    font-size: 22px;
    color: var(--ink-gray);
    letter-spacing: 1px;
  }
  .contact {
    position: absolute;
    right: 36px;
    top: 58px;
    text-align: right;
    font-family: "Raleway", sans-serif;
    color: var(--ink-gray);
  }
  .contact .person-name {
    font-weight: 300;
    font-size: 34px;
    color: var(--brand-green);
    line-height: 1;
    margin: 0;
  }
  .contact .name-rule {
    height: 1px;
    background: var(--rule-gray);
    margin: 6px 0 6px 0;
    width: 230px;
    margin-left: auto;
  }
  .contact .job-title {
    font-size: 16px;
    font-weight: 400;
    margin-bottom: 12px;
  }
  .contact .address {
    font-size: 13px;
    margin-bottom: 6px;
  }
  .contact .line {
    font-family: "Tinos", serif;
    font-size: 13px;
    line-height: 1.35;
  }

  /* Back */
  .card-back {
    background: var(--card-dark);
    color: var(--paper-white);
    font-family: "Tinos", serif;
  }
  .back-brand {
    position: absolute;
    left: 60px;
    top: 70px;
    display: flex;
    align-items: center;
    gap: 14px;
  }
  .back-brand .brand-square {
    background: var(--paper-white);
    width: 18px;
    height: 18px;
  }
  .back-brand .brand-name {
    font-size: 40px;
    color: var(--paper-white);
    line-height: 1;
  }
  .back-tagline {
    position: absolute;
    left: 92px;
    top: 124px;
    width: 300px;
    border-top: 1px solid var(--paper-white);
    padding-top: 4px;
    font-size: 10px;
    letter-spacing: 2.2px;
    text-transform: uppercase;
    color: #d6d6d6;
  }
  .lender-badge {
    position: absolute;
    right: 22px;
    top: 150px;
    width: 26px;
    height: 26px;
    border: 2px solid #8d8d8f;
    box-sizing: border-box;
  }
  .license-block {
    position: absolute;
    left: 28px;
    bottom: 26px;
    font-size: 12px;
    line-height: 1.7;
    color: #e3e3e3;
  }
  .license-block .referral-note {
    font-size: 13px;
    color: var(--paper-white);
  }
</style>
</head>
<body>
<main class="stage">
  <section class="card card-front" aria-label="Business card front">
    <div class="front-brand">
      <span class="brand-square"></span>
      <span class="brand-name">Torvan Lending</span>
    </div>
    <div class="contact">
      <h1 class="person-name">Ned Hartwell</h1>
      <div class="name-rule"></div>
      <div class="job-title">Finance Advisors</div>
      <div class="address">4172 Willow Crest Ln, San Ramon, CA 94583</div>
      <div class="line">Cell : 1234 089 555 010</div>
      <div class="line">Fax : 1234 089 555 010</div>
      <div class="line">ned@torvanlending.example</div>
    </div>
  </section>

  <section class="card card-back" aria-label="Business card back">
    <div class="back-brand">
      <span class="brand-square"></span>
      <span class="brand-name">Torvan Lending</span>
    </div>
    <div class="back-tagline">Your trusted mortgage advisors</div>
    <div class="lender-badge" role="img" aria-label="Equal housing lender badge"></div>
    <div class="license-block">
      <div>StaPLO License #</div>
      <div>HRQA #</div>
      <div class="referral-note">Manifest your trust in us through the gift of your referrals. We won't let you down</div>
    </div>
  </section>
</main>
</body>
</html>
```